300 x 250 Web Ad for Porn Website

300 x 250 web ad that will appear on a porn site. Need to see 3 options, one with each of the 3 girls. Remove the background around the girls.

Underneath the girls image should read in big bold letters: High Speed Internet
Underneath in slightly smaller size: NO Credit Check

To the left of the girl: Save MONEY...

To the right of the girl: So you can buy more PORN

We want it to look very unique, raunchy, and eye catching.

Target Market(s)

Porn website

Industry/Entity Type

Internet Service Provider

Colors

Designer to choose colors to be used in the design.

Requirements
Must have
• Must stand out so people will definitely notice it.
• JPEG and PNG formats

```html
<!DOCTYPE html>
<html lang="en">
<head>
<meta charset="utf-8">
<title>High Speed Internet – No Credit Check</title>
<link rel="stylesheet" href="https://fonts.googleapis.com/css2?family=Bowlby+One&family=Rubik:wght@700;800&display=swap">
<style>
  :root {
    --page: #ffffff;
    --ink-white: #ffffff;
    --ink-navy: #0b2f9f;
    --bg-red: #d0263a;
    --bg-purple: #7a1fa8;
    --bg-orange: #f3882f;
    --bg-yellow: #ffe08a;
    --bg-dark: #1a0510;
    --headline-stroke: #2a0508;
    --flare: #c77dff;
  }
  html, body {
    margin: 0;
    width: 1200px;
    height: 1192px;
    overflow: hidden;
    background: var(--page);
  }
  .ad {
    position: absolute;
    left: 0;
    top: 96px;
    width: 1200px;
    height: 1000px;
    overflow: hidden;
    background:
      radial-gradient(ellipse 420px 380px at 960px 160px, var(--bg-yellow) 0%, rgba(255,224,138,0) 70%),
      radial-gradient(ellipse 560px 520px at 1040px 360px, var(--bg-orange) 0%, rgba(243,136,47,0) 75%),
      radial-gradient(ellipse 520px 460px at 140px 180px, var(--bg-red) 0%, rgba(208,38,58,0) 80%),
      radial-gradient(ellipse 520px 460px at 330px 520px, var(--bg-purple) 0%, rgba(122,31,168,0) 80%),
      linear-gradient(180deg, #b0284a 0%, #6d1a6e 55%, var(--bg-dark) 100%);
  }
  .ad__model {
    position: absolute;
    left: 462px;
    top: 18px;
    width: 368px;
    height: 982px;
    border-radius: 160px 160px 40px 40px;
    background: linear-gradient(180deg, rgba(120,40,40,0.85) 0%, rgba(226,150,140,0.85) 35%, rgba(200,110,110,0.8) 70%, rgba(60,15,30,0.6) 100%);
  }
  .ad__shade {
    position: absolute;
    inset: 0;
    background: linear-gradient(180deg, rgba(0,0,0,0) 65%, rgba(20,3,10,0.75) 100%);
  }
  .ad__tease {
    position: absolute;
    margin: 0;
    font-family: "Rubik", sans-serif;
    font-weight: 800;
    line-height: 0.9;
    letter-spacing: -1px;
  }
  .ad__tease--left {
    left: 262px;
    top: 213px;
    color: var(--ink-white);
    font-size: 56px;
  }
  .ad__tease--right {
    left: 822px;
    top: 303px;
    color: var(--ink-navy);
    font-size: 50px;
  }
  .ad__tease--right span { display: block; padding-left: 44px; }
  .ad__tease--right span:first-child { padding-left: 0; }
  .ad__headlines {
    position: absolute;
    inset: 0;
  }
  .ad__headlines text {
    font-family: "Bowlby One", sans-serif;
    paint-order: stroke fill;
    stroke: var(--headline-stroke);
    stroke-linejoin: round;
  }
</style>
</head>
<body>
  <section class="ad">
    <div class="ad__model" role="img" aria-label="Photo cut-out of a model in a sheer lingerie bodysuit, standing centre"></div>
    <div class="ad__shade"></div>

    <p class="ad__tease ad__tease--left">Save<br>MONEY...</p>
    <p class="ad__tease ad__tease--right"><span>...So you can</span><span>buy more</span><span>PORN</span></p>

    <svg class="ad__headlines" viewBox="0 0 1200 1000" width="1200" height="1000" aria-hidden="false">
      <defs>
        <linearGradient id="orange-type" x1="0" y1="0" x2="0" y2="1">
          <stop offset="0" stop-color="#ffb15a"/>
          <stop offset="0.5" stop-color="#ff8a3d"/>
          <stop offset="0.52" stop-color="#ffc89a"/>
          <stop offset="1" stop-color="#ff7a45"/>
        </linearGradient>
        <linearGradient id="silver-type" x1="0" y1="0" x2="0" y2="1">
          <stop offset="0" stop-color="#ffffff"/>
          <stop offset="0.5" stop-color="#d9d9de"/>
          <stop offset="0.52" stop-color="#9a9aa4"/>
          <stop offset="1" stop-color="#e6e6ea"/>
        </linearGradient>
        <linearGradient id="flare-line" x1="0" y1="0" x2="1" y2="0">
          <stop offset="0" stop-color="#c77dff" stop-opacity="0"/>
          <stop offset="0.4" stop-color="#ffffff"/>
          <stop offset="1" stop-color="#c77dff" stop-opacity="0"/>
        </linearGradient>
      </defs>

      <g transform="rotate(-4 400 780)">
        <text x="150" y="700" font-size="112" fill="url(#orange-type)" stroke-width="14">HIGH</text>
        <text x="222" y="790" font-size="112" fill="url(#orange-type)" stroke-width="14">SPEED</text>
        <text x="72" y="910" font-size="126" fill="url(#orange-type)" stroke-width="14">INTERNET</text>
      </g>
      <path d="M300 820 L860 770 L300 826 Z" fill="url(#flare-line)" opacity="0.9"/>

      <g transform="rotate(-4 950 800)">
        <text x="860" y="770" font-size="78" fill="url(#silver-type)" stroke-width="12">NO</text>
        <text x="800" y="840" font-size="78" fill="url(#silver-type)" stroke-width="12">CREDIT</text>
        <text x="858" y="910" font-size="78" fill="url(#silver-type)" stroke-width="12">CHECK</text>
      </g>
      <path d="M760 870 L1200 820 L760 874 Z" fill="url(#flare-line)" opacity="0.6"/>
    </svg>
  </section>
</body>
</html>
```